Postcard Design

Domestic home cleaning business.......looking to call it " copper lantern" I would like to have a vastrelo bottle as the main feature.....on the bottle the centre lable shoild read I'M YOUR ALL PURPOSE CLEANER above the lable should read DON'T LIFT A FINGER! Then opposite the bottle 5 bullet points House Keeping, Washing,Ironing bed changing, END OF TENANCY CLEANS, MOVING IN CLEANS spring cleans.

On the back of the card Iwould like to list the following: At the top of the card it should read
THE ALL PURPOSE PERSONALISED CLEANER AND WHAT YOU CAN EXPECT

Reliable
Police checked and referenced cleaners
SAME CLEANER EVERY WEEK ON THE SAME DAY AND TIME TO BE AGREED BY YOU
ONLY EVER USE CUSTOMERS OWN PRODUCTS
EACH CLEAN INSURED
GENERAL HOUSE CLEANING AS WELL AS IRONING IF REQUIRED (min 2hours per week)

Reason: I have a couple of hospital appointments to attend this week after s major operation, so I need more time to concentrate......sorry

```html
<!DOCTYPE html>
<html lang="en">
<head>
<meta charset="utf-8">
<title>Copper Lantern – Postcard</title>
<link rel="stylesheet" href="https://fonts.googleapis.com/css2?family=Bebas+Neue&family=Oswald:wght@300;400;500&display=swap">
<style>
  :root {
    --backdrop: #0a0d0f;
    --sky: #bfeaf3;
    --paper: #ffffff;
    --headline-blue: #3cb6ee;
    --headline-red: #f2190f;
    --band: #49c6ec;
    --band-light: #8bdcf4;
    --tick: #f4e21b;
    --ink: #111111;
    --bottle-blue: #2a8fe0;
    --bottle-light: #8fd0f2;
    --glove-yellow: #e2d766;
  }
  html, body {
    margin: 0;
    padding: 0;
    width: 1200px;
    height: 1200px;
    overflow: hidden;
    background: var(--backdrop);
  }
  .postcard {
    position: absolute;
    left: 157px;
    top: 223px;
    width: 899px;
    height: 697px;
    overflow: hidden;
    background:
      radial-gradient(ellipse 60% 40% at 70% 5%, rgba(191,234,243,0.9), transparent 70%),
      linear-gradient(180deg, var(--sky) 0%, var(--paper) 22%, var(--paper) 60%, #dff4f8 80%, var(--paper) 100%);
  }
  .brand-name {
    position: absolute;
    left: 66px;
    top: 52px;
    margin: 0;
    font-family: "Bebas Neue", "Oswald", sans-serif;
    font-weight: 400;
    line-height: 0.82;
  }
  .brand-name .first-word {
    display: block;
    color: var(--headline-blue);
    font-size: 94px;
  }
  .brand-name .second-word {
    display: block;
    color: var(--headline-red);
    font-size: 150px;
    margin-top: 8px;
  }
  .services-band {
    position: absolute;
    left: 0;
    top: 285px;
    width: 560px;
    height: 210px;
    background:
      repeating-conic-gradient(from 0deg at 30% 50%, rgba(255,255,255,0.08) 0deg 3deg, transparent 3deg 8deg),
      linear-gradient(90deg, var(--band) 0%, var(--band-light) 100%);
  }
  .services-list {
    list-style: none;
    margin: 0;
    padding: 0;
    position: absolute;
    left: 66px;
    top: 292px;
  }
  .services-list li {
    display: flex;
    align-items: center;
    height: 38px;
    font-family: "Oswald", sans-serif;
    font-weight: 300;
    font-size: 24px;
    letter-spacing: 2.2px;
    color: var(--paper);
  }
  .services-list .tick {
    width: 22px;
    height: 20px;
    margin-right: 6px;
    flex: none;
  }
  .personal-details {
    position: absolute;
    left: 67px;
    top: 552px;
    margin: 0;
    font-family: "Oswald", sans-serif;
    font-weight: 500;
    font-size: 31px;
    letter-spacing: 0.5px;
    color: var(--ink);
    transform: scaleX(0.9);
    transform-origin: left center;
  }
  .product-photo {
    position: absolute;
    left: 560px;
    top: 77px;
    width: 339px;
    height: 620px;
    border-radius: 18px 0 0 0;
    background: linear-gradient(160deg, var(--glove-yellow) 0%, var(--bottle-light) 38%, var(--bottle-blue) 100%);
  }
</style>
</head>
<body>
  <section class="postcard">
    <h1 class="brand-name">
      <span class="first-word">COPPER</span>
      <span class="second-word">LANTERN</span>
    </h1>

    <div class="services-band"></div>
    <ul class="services-list">
      <li><svg class="tick" viewBox="0 0 22 20"><path d="M2 11 L8 17 L20 2" fill="none" stroke="var(--tick)" stroke-width="4" stroke-linecap="round" stroke-linejoin="round"/></svg>HOUSE KEEPING</li>
      <li><svg class="tick" viewBox="0 0 22 20"><path d="M2 11 L8 17 L20 2" fill="none" stroke="var(--tick)" stroke-width="4" stroke-linecap="round" stroke-linejoin="round"/></svg>WASHING</li>
      <li><svg class="tick" viewBox="0 0 22 20"><path d="M2 11 L8 17 L20 2" fill="none" stroke="var(--tick)" stroke-width="4" stroke-linecap="round" stroke-linejoin="round"/></svg>IRONING BED CHANGING</li>
      <li><svg class="tick" viewBox="0 0 22 20"><path d="M2 11 L8 17 L20 2" fill="none" stroke="var(--tick)" stroke-width="4" stroke-linecap="round" stroke-linejoin="round"/></svg>END OF TENANCY CLEANS</li>
      <li><svg class="tick" viewBox="0 0 22 20"><path d="M2 11 L8 17 L20 2" fill="none" stroke="var(--tick)" stroke-width="4" stroke-linecap="round" stroke-linejoin="round"/></svg>MOVING IN CLEANS SPRING CLEANS</li>
    </ul>

    <p class="personal-details">PERSONAL DETAILS</p>

    <div class="product-photo" role="img" aria-label="Photo of a yellow-gloved hand holding a blue Vastrelo all purpose cleaner spray bottle with a red trigger, water splashing around its base"></div>
  </section>
</body>
</html>
```